Letter Head Design - Finance industry

Design a letterhead to match the logo. Needs to be clean, simple and crisp. I'm open to suggestions. Will be using the logo that was submitted last with the W crossed over

Target Market(s)

Small medium businesses and government department's

Industry/Entity Type

Industry

Font styles to use
Sans Serif

Colors
cadf82
bcd85c
acd036
9bcb3c
e9e9e9
aaaaaa
000000
7f7f7f
b7b7b7

Requirements
Must have
• Need to display: Logo, Business address, ABN number, ASIC register number, contact phone, website, company email. Details are as per below:

Suite 4B Level 17
Marlowe Crest House
9 Tindall Lane
Sydney NSW 2000
Landline Ph: 02 5193 4620
Ph: 1300 4719 55
Email: enquiries@coinharbourco.com.au
W: www.coinharbourco.com.au

On the footer, the details below need to be specified:
ABN: 47 381 950 623
ASIC Registration Number: 31 749218605

Should not have
• No imagery or design that is not in line with the logo

```html
<!DOCTYPE html>
<html lang="en">
<head>
<meta charset="utf-8">
<title>Coin Harbour Co Letterhead</title>
<link href="https://fonts.googleapis.com/css2?family=Arimo:wght@400&family=Open+Sans:wght@400;600&display=swap" rel="stylesheet">
<style>
  :root {
    --backdrop: #2e2e2e;
    --paper: #f6f8f7;
    --green: #9bcb3c;
    --grey: #7f7f7f;
    --grey-light: #e9e9e9;
    --ink: #000000;
    --white: #ffffff;
  }
  * { margin: 0; padding: 0; box-sizing: border-box; }
  html, body { width: 999px; height: 1200px; overflow: hidden; }
  body { background: var(--backdrop); position: relative; }
  .letterhead {
    position: absolute; left: 119px; top: 63px;
    width: 761px; height: 1074px;
    background: var(--paper); overflow: hidden;
  }
  .letterhead__art { position: absolute; inset: 0; width: 761px; height: 1074px; }
  .brand {
    position: absolute; left: 84px; top: 50px;
    font-family: "Open Sans", sans-serif; font-weight: 600;
    font-size: 26px; color: var(--white); letter-spacing: -0.3px;
    display: flex; align-items: center; gap: 10px;
  }
  .brand__dot { width: 10px; height: 10px; border-radius: 50%; background: var(--white); }
  .address {
    position: absolute; left: 586px; top: 35px;
    font-family: "Open Sans", sans-serif; font-size: 11.5px; line-height: 15.5px;
    color: var(--white); list-style: none;
  }
  .letter-body {
    position: absolute; left: 44px; top: 246px; width: 668px;
    font-family: "Arimo", Arial, sans-serif; font-size: 14.1px; line-height: 18px;
    color: var(--ink); text-align: justify;
  }
  .letter-body p + p { margin-top: 18px; }
  .signature {
    position: absolute; left: 578px; top: 862px; width: 112px; height: 80px;
    background: var(--grey-light); opacity: .5; border-radius: 4px;
  }
  .footer-text {
    position: absolute; font-family: "Open Sans", sans-serif;
    font-size: 11.5px; line-height: 16px; color: var(--white); list-style: none;
  }
  .footer-text li { display: flex; align-items: center; gap: 8px; }
  .footer-text svg { width: 11px; height: 11px; flex: none; }
  .footer-text--web { left: 44px; top: 1026px; }
  .footer-text--phone { left: 333px; top: 1026px; }
  .footer-text--reg { left: 467px; top: 1026px; }
  .footer-divider {
    position: absolute; left: 445px; top: 1020px; width: 1px; height: 38px;
    background: var(--grey-light);
  }
</style>
</head>
<body>
<main class="letterhead">
  <svg class="letterhead__art" viewBox="0 0 761 1074" aria-hidden="true">
    <defs>
      <linearGradient id="headerGrey" x1="0" y1="0" x2="1" y2="0">
        <stop offset="0" stop-color="#6f6f6f"/>
        <stop offset="1" stop-color="#8a8a8a"/>
      </linearGradient>
      <linearGradient id="silver" x1="0" y1="0" x2="1" y2="0">
        <stop offset="0" stop-color="#b7b7b7"/>
        <stop offset=".55" stop-color="#7f7f7f"/>
        <stop offset="1" stop-color="#e9e9e9"/>
      </linearGradient>
    </defs>
    <path d="M470 0 H761 V200 C690 150 590 114 455 112 Z" fill="var(--green)"/>
    <path d="M0 0 H575 C545 45 510 85 470 108 C400 122 330 112 255 100 C170 88 80 80 0 84 Z" fill="url(#headerGrey)"/>
    <path d="M0 86 C80 82 170 90 255 102 C330 114 400 124 470 110" stroke="url(#silver)" stroke-width="5" fill="none"/>
    <path d="M0 953 C80 985 180 1008 310 1018 L310 1074 H0 Z" fill="var(--green)"/>
    <path d="M200 1074 C270 1028 390 1000 510 1000 C620 1000 700 1018 761 1040 V1074 Z" fill="var(--grey)"/>
    <path d="M220 1060 C300 1018 400 998 510 998 C620 998 700 1016 761 1036" stroke="url(#silver)" stroke-width="4" fill="none"/>
  </svg>

  <div class="brand"><span class="brand__dot"></span>Coin Harbour Co</div>

  <ul class="address">
    <li>Suite 4B Level 17</li>
    <li>Marlowe Crest House</li>
    <li>9 Tindall Lane</li>
    <li>Sydney NSW 2000</li>
  </ul>

  <article class="letter-body">
    <p>Lorem ipsum dolor sit amet, consectetur adipiscing elit. Proin porta, turpis sed elementum semper, est enim viverra nulla, non sollicitudin lorem felis ac enim. Duis varius arcu sed ipsum sollicitudin, vitae consequat ligula rhoncus. Donec blandit quam quis dui lobortis consequat. Vivamus in tempor turpis, sed mollis lacus. Maecenas ac libero erat. Suspendisse elit lacus, bibendum et arcu nec, malesuada vulputate nunc. Nunc enim ex, placerat sit amet porta eu, consequat a risus.</p>
    <p>Lorem ipsum dolor sit amet, consectetur adipiscing elit. Vestibulum pharetra enim at rutrum imperdiet. Aliquam sollicitudin efficitur purus. Integer eros lacus, pellentesque sed ornare eget, imperdiet lacinia est. Sed egestas erat eget erat dictum, et mattis lorem bibendum. Quisque at tellus egestas, finibus augue vel, semper urna. Donec facilisis mi in dui imperdiet, vel aliquet eros hendrerit. Nulla facilisi.</p>
    <p>Nam ipsum purus, pellentesque ac placerat quis, rhoncus quis nisl. Vivamus gravida placerat magna, quis vestibulum odio tincidunt quis. Fusce vitae tristique ipsum. Nam sed velit accumsan quam elementum venenatis. Sed non neque eget felis vulputate condimentum. Nunc ultrices in metus a congue. Maecenas ut erat eget orci feugiat pulvinar quis vitae libero. Sed finibus risus pellentesque libero malesuada hendrerit. Cum sociis natoque penatibus et magnis dis parturient montes, nascetur ridiculus mus. Vestibulum malesuada purus urna, pretium bibendum est iaculis id. Nullam dui arcu, gravida at felis eu, varius venenatis nunc. Sed rutrum pellentesque erat, finibus feugiat nunc porta ac.</p>
    <p>Morbi fringilla malesuada arcu, viverra congue mauris pellentesque sed. Duis elementum faucibus nulla, sit amet sodales lectus scelerisque sed. Pellentesque egestas lorem nulla, vel facilisis urna ultrices ac. Pellentesque ac felis in orci porttitor viverra. Integer tortor nunc, pulvinar id neque nec, convallis rutrum sem. Mauris sed velit erat. Nunc tincidunt, dui ut aliquet consequat, lorem justo accumsan nisi, eget mollis nisl erat non ante. Proin luctus mollis nibh, sit amet placerat mi tempus vel.</p>
    <p>Suspendisse finibus urna sed maximus mollis. Maecenas sit amet suscipit sapien. Donec a justo quis felis pellentesque sodales condimentum non risus. Ut dignissim pellentesque augue, id pharetra odio vulputate eget. Nam non porttitor sapien. Proin iaculis nisi a neque ultrices porta. Curabitur eu congue quam. Lorem ipsum dolor sit amet, consectetur adipiscing elit. Curabitur accumsan at augue ac vestibulum. Sed sed mattis velit. Proin eros risus, viverra nec urna ac, convallis fringilla massa. Pellentesque elementum ligula a sem sollicitudin mattis. Suspendisse eget pretium felis.</p>
  </article>

  <div class="signature" role="img" aria-label="Handwritten signature of the sender"></div>

  <ul class="footer-text footer-text--web">
    <li><svg viewBox="0 0 12 12"><rect x="1" y="2.5" width="10" height="7" rx="1" fill="none" stroke="#fff" stroke-width="1.2"/><path d="M1.5 3 L6 6.5 L10.5 3" fill="none" stroke="#fff" stroke-width="1.1"/></svg>enquiries@coinharbourco.com.au</li>
    <li><svg viewBox="0 0 12 12"><circle cx="6" cy="6" r="5" fill="none" stroke="#fff" stroke-width="1.2"/><path d="M1 6 H11 M6 1 C3.5 4 3.5 8 6 11 M6 1 C8.5 4 8.5 8 6 11" fill="none" stroke="#fff" stroke-width="1"/></svg>www.coinharbourco.com.au</li>
  </ul>

  <ul class="footer-text footer-text--phone">
    <li><svg viewBox="0 0 12 12"><path d="M2.5 1.5 L4.5 1.5 L5.3 4 L4 5 C4.7 6.5 5.5 7.3 7 8 L8 6.7 L10.5 7.5 L10.5 9.5 C10.5 10.2 10 10.5 9.4 10.5 C5 10.2 1.8 7 1.5 2.6 C1.5 2 1.8 1.5 2.5 1.5 Z" fill="#fff"/></svg>02 5193 4620</li>
    <li><svg viewBox="0 0 12 12"><rect x="3" y="1" width="6" height="10" rx="1.2" fill="none" stroke="#fff" stroke-width="1.2"/><circle cx="6" cy="9" r=".7" fill="#fff"/></svg>1300 4719 55</li>
  </ul>

  <div class="footer-divider"></div>

  <ul class="footer-text footer-text--reg">
    <li>ABN: 47 381 950 623</li>
    <li>ASIC: Registration Number: 31 749218605</li>
  </ul>
</main>
</body>
</html>
```